Amber Hollow Productions

I need a business card design for a new freelance film production company using or incorporating the logo:
I want the card to be creative, minimal, yet professional. Feel free to use a variety of different shapes and sizes/ textures for the card.

Industry/Entity Type

Film Production

```html
<!DOCTYPE html>
<html lang="en">
<head>
<meta charset="utf-8">
<title>Amber Hollow Productions — Business Cards</title>
<link rel="stylesheet" href="https://fonts.googleapis.com/css2?family=Jost:ital,wght@0,300;0,400;1,300&display=swap">
<style>
  :root {
    --backdrop: #c9d2d1;
    --card: #ffffff;
    --brand-blue: #2f63e4;
    --muted-grey: #8a9190;
    --card-shadow: rgba(40, 50, 50, 0.28);
  }
  * { margin: 0; padding: 0; box-sizing: border-box; }
  html, body {
    width: 1200px;
    height: 1200px;
    overflow: hidden;
  }
  body {
    background: var(--backdrop);
    font-family: "Jost", "Futura", sans-serif;
    position: relative;
  }
  .card {
    position: absolute;
    background: var(--card);
    box-shadow: 6px 8px 18px var(--card-shadow);
    display: flex;
    flex-direction: column;
    align-items: center;
    justify-content: center;
  }
  .card-front {
    left: 110px;
    top: 250px;
    width: 620px;
    height: 352px;
  }
  .card-back {
    left: 430px;
    top: 540px;
    width: 700px;
    height: 400px;
  }
  .wordmark {
    display: flex;
    align-items: center;
    gap: 18px;
    color: var(--brand-blue);
    font-weight: 400;
    text-transform: uppercase;
  }
  .wordmark-square {
    width: 34px;
    height: 34px;
    background: var(--brand-blue);
    flex: none;
  }
  .wordmark-name {
    font-size: 40px;
    line-height: 1.1;
    letter-spacing: 2px;
  }
  .wordmark-name .line-sub {
    display: block;
    font-size: 40px;
    letter-spacing: 9px;
  }
  .card-back .wordmark-name { font-size: 22px; letter-spacing: 3px; }
  .card-back .wordmark-square { width: 20px; height: 20px; }
  .card-back .wordmark { gap: 12px; margin-bottom: 34px; }
  .holder {
    text-align: right;
  }
  .holder-name {
    color: var(--brand-blue);
    font-weight: 400;
    font-size: 44px;
    letter-spacing: 1px;
    line-height: 1;
    text-transform: uppercase;
  }
  .holder-role {
    color: var(--muted-grey);
    font-weight: 300;
    font-style: italic;
    font-size: 15px;
    margin-top: 2px;
  }
  .contact {
    margin-top: 38px;
    text-align: center;
    color: var(--brand-blue);
    font-weight: 400;
    font-size: 13px;
    line-height: 1.6;
  }
  .contact-web { letter-spacing: 3px; }
</style>
</head>
<body>
  <section class="card card-front">
    <div class="wordmark">
      <span class="wordmark-square"></span>
      <span class="wordmark-name">Amber Hollow<span class="line-sub">Productions</span></span>
    </div>
  </section>

  <section class="card card-back">
    <div class="wordmark">
      <span class="wordmark-square"></span>
      <span class="wordmark-name">Amber Hollow Productions</span>
    </div>
    <div class="holder">
      <div class="holder-name">Jordan Vale</div>
      <div class="holder-role">founder</div>
    </div>
    <div class="contact">
      <div class="contact-phone">555.014.2290</div>
      <div class="contact-email">jordan@amberhollowstudios.com</div>
      <div class="contact-web">www.amberhollowstudios.com</div>
    </div>
  </section>
</body>
</html>
```